poster for escape room advertising the themes of our rooms, bold, samples attached

we need poster advertising our 4 escape room themes. The Crimson Ledger, (doctor, test tube) Midnight Carnival, (retro items, time machine) The Velvet Parlour (serial killer, clown, doll, knives) and , moonspire (island, ship, compass). Primarily black and white with red and yellow.
samples attached. Comic book or bold graphic theme. More information can be found on our website quillgatepuzzles.com.

• impact, anything bold, almost comic book

fbee3c
ec1f27
ffffff
000000
5c5c5c
9d9d9d
cbcbcb
e8e8e8
cfcfcf

• title of each room, The Crimson Ledger, Midnight Carnival, The Velvet Parlour, Moonspire. Graphic representing each theme.
• short description of rooms

```html
<!DOCTYPE html>
<html lang="en">
<head>
<meta charset="utf-8">
<title>Quillgate TX Escape Rooms</title>
<link href="https://fonts.googleapis.com/css2?family=Anton&family=Bangers&family=Oswald:wght@600&family=Roboto+Condensed:wght@700&display=swap" rel="stylesheet">
<style>
  :root {
    --yellow: #fbee3c;
    --red: #ec1f27;
    --white: #ffffff;
    --black: #000000;
    --grey-dark: #5c5c5c;
    --grey-mid: #9d9d9d;
    --grey-light: #cbcbcb;
    --grey-pale: #e8e8e8;
  }
  html, body { margin: 0; padding: 0; overflow: hidden; background: var(--black); }
  .poster {
    position: relative; width: 849px; height: 1200px; overflow: hidden;
    background: var(--black); font-family: "Roboto Condensed", sans-serif;
  }
  .abs { position: absolute; }
  .header-city {
    left: 50px; top: 18px; margin: 0; color: var(--yellow);
    font-family: "Anton", sans-serif; font-size: 40px; letter-spacing: 1px; line-height: 1;
  }
  .header-title {
    left: 40px; top: 58px; margin: 0; width: 770px; color: var(--yellow);
    font-family: "Anton", sans-serif; font-size: 100px; line-height: 1; letter-spacing: 1px;
    display: flex; justify-content: space-between;
  }
  .frame-art { left: 0; top: 0; }
  .room-title {
    margin: 0; color: var(--yellow); font-family: "Bangers", sans-serif; line-height: .86;
    -webkit-text-stroke: 3px var(--black); paint-order: stroke fill;
    text-shadow: 4px 4px 0 var(--black); letter-spacing: 1px; text-align: center;
  }
  .caption {
    margin: 0; background: var(--white); border: 2px solid var(--black); color: var(--black);
    font-size: 13.5px; line-height: 1.2; text-transform: uppercase; padding: 8px 10px; box-sizing: border-box;
  }
  .placeholder { border-radius: 6px; }
  .footer { top: 1100px; color: var(--yellow); font-family: "Oswald", sans-serif; font-size: 15px; line-height: 1.45; }
  .footer p { margin: 0; }
  .footer-brand {
    left: 366px; top: 1104px; width: 118px; text-align: center; color: var(--white);
    font-family: "Oswald", sans-serif; font-size: 15px; line-height: 1.1; letter-spacing: 1px; text-transform: uppercase;
  }
  .footer-brand .mark { display: block; width: 40px; height: 40px; margin: 0 auto 6px; background: var(--grey-dark); }
</style>
</head>
<body>
<main class="poster">
  <h2 class="abs header-city">QUILLGATE TX</h2>
  <h1 class="abs header-title"><span>ESCAPE</span><span>ROOMS</span></h1>

  <svg class="abs frame-art" width="849" height="1200" viewBox="0 0 849 1200" role="img" aria-label="Comic panels filled with scratchy black ink texture">
    <defs>
      <linearGradient id="panelTone" x1="0" y1="0" x2="1" y2="1">
        <stop offset="0" stop-color="#e8e8e8"/>
        <stop offset=".5" stop-color="#cbcbcb"/>
        <stop offset="1" stop-color="#e8e8e8"/>
      </linearGradient>
      <linearGradient id="dripTone" x1="0" y1="0" x2="1" y2="0">
        <stop offset="0" stop-color="#ec1f27"/>
        <stop offset=".6" stop-color="#fbee3c"/>
        <stop offset="1" stop-color="#ec1f27"/>
      </linearGradient>
    </defs>
    <polyline points="432,6 420,44 432,58 412,160" fill="none" stroke="#fff" stroke-width="4"/>
    <rect x="44" y="164" width="762" height="906" fill="#fff"/>
    <polygon points="50,180 414,180 414,622 50,630" fill="url(#panelTone)" stroke="#000" stroke-width="3"/>
    <polygon points="424,170 800,170 800,650 424,660" fill="url(#panelTone)" stroke="#000" stroke-width="3"/>
    <polygon points="50,640 414,632 414,1064 50,1064" fill="url(#panelTone)" stroke="#000" stroke-width="3"/>
    <polygon points="424,670 800,660 800,1064 424,1064" fill="url(#panelTone)" stroke="#000" stroke-width="3"/>
    <polygon points="50,640 414,632 414,760 380,900 340,760 300,820 250,700 180,720 120,680 50,720" fill="url(#dripTone)"/>
    <polygon points="164,220 186,272 236,234 226,296 296,290 246,336 306,372 240,392 280,446 214,436 210,506 170,456 128,512 120,446 56,470 90,410 50,380 104,352 66,300 128,306 120,240" fill="#ec1f27"/>
    <polygon points="440,470 800,250 800,650" fill="#ec1f27"/>
    <circle cx="672" cy="985" r="138" fill="#ec1f27"/>
  </svg>

  <div class="abs placeholder" role="img" aria-label="Black silhouette of a running figure" style="left:410px;top:400px;width:120px;height:320px;background:radial-gradient(ellipse at center,#000 45%,rgba(0,0,0,0) 72%);"></div>
  <div class="abs placeholder" role="img" aria-label="Ink drawing of a creepy clown figure" style="left:270px;top:790px;width:120px;height:140px;background:radial-gradient(ellipse at center,#5c5c5c 0%,rgba(157,157,157,0) 70%);"></div>
  <div class="abs placeholder" role="img" aria-label="Ink drawing of a compass rose" style="left:640px;top:650px;width:130px;height:120px;background:radial-gradient(circle at center,#5c5c5c 0%,rgba(203,203,203,0) 68%);"></div>

  <h3 class="abs room-title" style="left:64px;top:282px;width:210px;font-size:56px;transform:rotate(-9deg);">THE CRIMSON LEDGER</h3>
  <p class="abs caption" style="left:84px;top:500px;width:300px;transform:rotate(-4deg);">Millions of people across the world have been infected with a life-threatening virus. Dr. Marlowe-Quist was working on a cure that could save lives across the globe, but has just died...</p>

  <p class="abs caption" style="left:428px;top:212px;width:322px;border:none;background:var(--white);transform:rotate(-5deg);">Unlock the door, or you will be sent back for eternity to the 90s, the age of hedgehogs, beepers, singing purple dinosaurs, cassette tapes, and inflatable furniture.</p>
  <h3 class="abs room-title" style="left:580px;top:360px;width:220px;font-size:66px;transform:rotate(-10deg);">MIDNIGHT CARNIVAL</h3>

  <h3 class="abs room-title" style="left:56px;top:672px;width:340px;font-size:72px;text-align:left;transform:rotate(-6deg);">THE VELVET PARLOUR</h3>
  <p class="abs caption" style="left:86px;top:940px;width:344px;transform:rotate(-6deg);">On a quest to save your friend, you find yourself trapped in the lair of a murderous psychopath. As you search for a way to escape, you must find out where your friend is and how to save them.</p>

  <p class="abs caption" style="left:452px;top:790px;width:300px;transform:rotate(-9deg);">You are trapped on a desert island, the only way to escape is to alert passing boats or building a raft. In the meantime you need to find water to survive.</p>
  <h3 class="abs room-title" style="left:582px;top:950px;width:200px;font-size:64px;transform:rotate(-8deg);">MOONSPIRE</h3>

  <div class="abs footer" style="left:172px;">
    <p>QUILLGATE, 1418 Harlow Lane</p>
    <p>Suite 204, Fenwick TX</p>
    <p>www.quillgatepuzzles.com</p>
  </div>
  <div class="abs footer-brand"><span class="mark"></span>Quillgate Puzzles</div>
  <div class="abs footer" style="left:504px;">
    <p>BOOK TODAY!</p>
    <p>(555) 014-2287</p>
    <p>info@quillgatepuzzles.com</p>
  </div>
</main>
</body>
</html>
```